web page layout, style , color, font & flow design

We are developing a single page application. The SPA (single page application) will display natural gas pipeline flow data once the customer logs on. The customer has a choice of the region, the pipeline, the zone on the pipeline, whether the point is a delivery point or receipt point and the state the pipeline flows through.
we have jumpstarted the project and are attaching a pdf of the same.

we are using mockingbird for the wireframe. any designer is free to use this tool to make changes.

A mockingbird wireframe link is added below. you are free to use it and to make changes. please save the changed wireframe in a different name

we are looking for inputs on layout, style , color, font & flow.

A logo jpg file has also been attached.

Target Market(s)

this single web page is going to be used by natural gas traders and schedulers day in and day out. the application is more of business to business corporate application.

Industry/Entity Type

Delivery

Requirements
Must have
• layout ,flow, size, color, font , ease of use.

```html
<!DOCTYPE html>
<html lang="en">
<head>
<meta charset="utf-8">
<title>Pipeline Flow Dashboard</title>
<link href="https://fonts.googleapis.com/css2?family=Open+Sans:wght@400;600;700&display=swap" rel="stylesheet">
<style>
:root{
  --blue:#0a6abf;
  --blue-btn:#3d8fd6;
  --blue-btn-dark:#2f7cc2;
  --green:#8cc63f;
  --pink:#e6336f;
  --orange:#f26522;
  --navy:#1b5fa8;
  --side-bg:#e6e6e6;
  --side-line:#f4f4f4;
  --text:#333;
  --muted:#777;
  --line:#e2e2e2;
  --red:#ef3e4a;
  --purple:#c59fdc;
  --footer:#2c2c2c;
  --page-grey:#efefef;
}
*{box-sizing:border-box;margin:0;padding:0}
html,body{width:1116px;height:1200px;overflow:hidden;background:#fff}
body{font-family:"Open Sans",sans-serif;color:var(--text);position:relative}

/* header */
.topbar{position:absolute;left:0;top:0;width:1116px;height:46px;border-bottom:2px solid #ddd}
.brand{position:absolute;left:66px;top:11px;display:flex;align-items:center;gap:6px;font-weight:700;font-size:15px;color:var(--navy)}
.brand-dot{width:18px;height:18px;border-radius:50%;background:var(--green)}
.user-tools{position:absolute;right:44px;top:0;display:flex;height:46px}
.user-name{width:88px;background:var(--green);color:#fff;font-weight:700;font-size:13px;display:flex;align-items:center;justify-content:center}
.tool{width:44px;display:flex;align-items:center;justify-content:center;position:relative}
.tool.mail{background:var(--pink)}
.tool.alert{background:var(--orange)}
.tool.power{background:var(--navy)}
.badge{position:absolute;right:3px;top:1px;color:#fff;font-size:12px}

/* sidebar */
.sidebar{position:absolute;left:0;top:46px;width:193px}
.menu-head{height:45px;background:var(--blue);color:#fff;display:flex;align-items:center;justify-content:center;gap:44px;font-size:16px}
.nav-item{height:53px;background:var(--side-bg);border-bottom:1px solid var(--side-line);display:flex;align-items:center;padding:0 0 0 16px;font-size:14px;color:#444;position:relative}
.nav-item svg{width:26px;height:22px;margin-right:12px}
.nav-item .chev{position:absolute;right:18px;top:19px;width:10px;height:14px;margin:0}
.news-head{margin-top:38px;height:45px;background:var(--blue);color:#fff;display:flex;align-items:center;justify-content:center;gap:26px;font-size:16px}
.news-mark{width:22px;height:22px;border-radius:50%;background:#fff}
.news-list{background:var(--side-bg);height:236px;padding-top:14px}
.tweet{display:flex;padding:9px 0 0 12px;height:67px}
.tweet-mark{width:30px;height:30px;border-radius:50%;background:var(--green);margin-top:6px;flex:none}
.tweet-body{margin-left:20px;font-size:8px;line-height:10.5px;color:#222}
.tweet-body b{font-size:10px;display:block;line-height:12px}
.tweet-body .link{font-weight:700}

/* main */
.page-title{position:absolute;left:225px;top:52px;font-size:24px;font-weight:400;color:#333}
.filters{position:absolute;left:221px;top:115px;display:flex}
.dd{height:29px;display:flex;background:var(--blue-btn);color:#fff;font-size:13px;margin-right:4px;border-radius:2px}
.dd span{flex:1;display:flex;align-items:center;justify-content:center}
.dd i{width:20px;background:var(--blue-btn-dark);display:flex;align-items:center;justify-content:center}
.dd i::after{content:"";border:4px solid transparent;border-top-color:#fff;margin-top:4px}
.datepick{position:absolute;top:115px;height:29px;width:110px;border:1px solid var(--blue-btn);display:flex;color:var(--blue-btn);font-size:13px;border-radius:2px}
.datepick span{flex:1;display:flex;align-items:center;justify-content:center}
.datepick i{width:22px;background:var(--blue-btn);display:flex;align-items:center;justify-content:center}

.data-panel{position:absolute;left:220px;top:171px;width:852px;height:466px;border:1px solid #ddd;border-radius:3px}
.refresh{position:absolute;right:12px;top:8px}
table{position:absolute;left:13px;top:24px;width:832px;border-collapse:collapse;font-size:12.5px}
th{text-align:left;font-weight:600;height:33px;border-bottom:1px solid var(--line);padding-left:8px;white-space:nowrap}
td{height:32.5px;border-bottom:1px solid var(--line);padding-left:8px;white-space:nowrap}
th:first-child,td:first-child{width:43px}

.pager{position:absolute;left:220px;top:664px;display:flex;gap:22px}
.pg{width:51px;height:31px;background:#eee;font-size:10px;font-weight:700;display:flex;align-items:center;justify-content:center;color:#333}
.pg.on{background:#555;color:#fff}
.pg.next{background:var(--blue);color:#fff}

.chart-tabs{position:absolute;left:220px;top:739px;width:151px}
.tab-head{height:52px;background:var(--blue);color:#fff;font-weight:700;font-size:13px;display:flex;align-items:center;justify-content:center}
.tab{height:54px;background:#f5f5f5;border-bottom:1px solid #fff;display:flex;align-items:center;justify-content:center;font-weight:700;font-size:12.5px;color:#333}
.tab.on{color:var(--blue);border-left:4px solid var(--blue);width:172px;background:#f5f5f5}
.chart-panel{position:absolute;left:396px;top:740px;width:676px;height:317px;background:var(--page-grey)}
.chart-panel svg{display:block}

.footer{position:absolute;left:0;top:1138px;width:1116px;height:62px;background:var(--footer);color:#aaa;font-size:12.5px;display:flex;align-items:center;justify-content:space-between;padding:0 82px 0 80px}
.footer b{color:#aaa}
.footer nav{color:#bbb}
</style>
</head>
<body>

<header class="topbar">
  <div class="brand"><span class="brand-dot"></span>GasFlow</div>
  <div class="user-tools">
    <div class="user-name">User Name</div>
    <div class="tool mail">
      <svg width="28" height="20" viewBox="0 0 28 20"><rect x="1" y="1" width="26" height="18" fill="#fff"/><path d="M1 1 L14 11 L27 1" fill="none" stroke="#e6336f" stroke-width="2"/></svg>
      <span class="badge">5</span>
    </div>
    <div class="tool alert">
      <svg width="28" height="26" viewBox="0 0 28 26"><path d="M14 1 L27 25 H1 Z" fill="#fff"/><rect x="12.5" y="8" width="3" height="10" fill="#f26522"/><rect x="12.5" y="20" width="3" height="3" fill="#f26522"/></svg>
      <span class="badge">3</span>
    </div>
    <div class="tool power">
      <svg width="26" height="26" viewBox="0 0 26 26"><path d="M8 6 A10 10 0 1 0 18 6" fill="none" stroke="#fff" stroke-width="3"/><line x1="13" y1="2" x2="13" y2="13" stroke="#fff" stroke-width="3"/></svg>
    </div>
  </div>
</header>

<aside class="sidebar">
  <div class="menu-head">MENU
    <svg width="22" height="18" viewBox="0 0 22 18"><rect y="0" width="22" height="3" fill="#fff"/><rect y="5" width="22" height="3" fill="#fff"/><rect y="10" width="22" height="3" fill="#fff"/><rect y="15" width="22" height="3" fill="#fff"/></svg>
  </div>
  <div class="nav-item"><svg viewBox="0 0 26 22"><circle cx="13" cy="11" r="10" fill="none" stroke="#444" stroke-width="1.5"/><ellipse cx="13" cy="11" rx="4.5" ry="10" fill="none" stroke="#444"/><line x1="3" y1="11" x2="23" y2="11" stroke="#444"/></svg>Regions<svg class="chev" viewBox="0 0 10 14"><path d="M2 1 L8 7 L2 13" fill="none" stroke="#fff" stroke-width="2"/></svg></div>
  <div class="nav-item"><svg viewBox="0 0 26 22"><path d="M2 16 L8 9 L13 14 L18 8 L24 14" fill="none" stroke="#444" stroke-width="1.8"/></svg>Pipelines<svg class="chev" viewBox="0 0 10 14"><path d="M2 1 L8 7 L2 13" fill="none" stroke="#fff" stroke-width="2"/></svg></div>
  <div class="nav-item"><svg viewBox="0 0 26 22"><path d="M2 19 L8 12 L13 16 L19 9" fill="none" stroke="#444" stroke-width="1.8"/><path d="M20 1 V9 M16 5 H24" stroke="#444" stroke-width="1.6"/></svg>add Pipelines<svg class="chev" viewBox="0 0 10 14"><path d="M2 1 L8 7 L2 13" fill="none" stroke="#fff" stroke-width="2"/></svg></div>
  <div class="nav-item"><svg viewBox="0 0 26 22"><path d="M23 2 L3 10 L10 13 L13 20 Z M10 13 L23 2" fill="none" stroke="#444" stroke-width="1.6" stroke-linejoin="round"/></svg>Contact us<svg class="chev" viewBox="0 0 10 14"><path d="M2 1 L8 7 L2 13" fill="none" stroke="#fff" stroke-width="2"/></svg></div>
  <div class="nav-item"><svg viewBox="0 0 26 22"><circle cx="13" cy="5.5" r="5" fill="#333"/><rect x="5" y="12" width="16" height="10" rx="4" fill="#333"/></svg>Help Desk<svg class="chev" viewBox="0 0 10 14"><path d="M2 1 L8 7 L2 13" fill="none" stroke="#fff" stroke-width="2"/></svg></div>

  <div class="news-head">LATEST NEWS <span class="news-mark"></span></div>
  <div class="news-list">
    <div class="tweet"><span class="tweet-mark"></span><div class="tweet-body"><b>@GasFlow</b>Lorem ipsum dolor sit amet,<br>consectetur adipiscing elit<br><span class="link">http://lnk.example/a7Kq2Rz</span></div></div>
    <div class="tweet"><span class="tweet-mark"></span><div class="tweet-body"><b>@GasFlow</b>Lorem ipsum dolor sit amet,<br>consectetur adipiscing elit<br><span class="link">http://lnk.example/a7Kq2Rz</span></div></div>
    <div class="tweet"><span class="tweet-mark"></span><div class="tweet-body"><b>@GasFlow</b>Lorem ipsum dolor sit amet,<br>consectetur adipiscing elit<br><span class="link">http://lnk.example/a7Kq2Rz</span></div></div>
  </div>
</aside>

<h1 class="page-title">NorthEast Ridgeline</h1>

<div class="filters">
  <div class="dd" style="width:87px"><span>Region</span><i></i></div>
  <div class="dd" style="width:92px"><span>Pipelines</span><i></i></div>
  <div class="dd" style="width:121px"><span>Location Type</span><i></i></div>
  <div class="dd" style="width:81px"><span>States</span><i></i></div>
  <div class="dd" style="width:80px"><span>Zones</span><i></i></div>
  <div class="dd" style="width:121px"><span>Cycle Info</span><i></i></div>
</div>
<div class="datepick" style="left:837px"><span>Gasday</span><i><svg width="10" height="10" viewBox="0 0 10 10"><rect x="0.5" y="1.5" width="9" height="8" fill="none" stroke="#fff"/><rect x="0.5" y="1.5" width="9" height="2" fill="#fff"/></svg></i></div>
<div class="datepick" style="left:961px"><span>Posting</span><i><svg width="10" height="10" viewBox="0 0 10 10"><rect x="0.5" y="1.5" width="9" height="8" fill="none" stroke="#fff"/><rect x="0.5" y="1.5" width="9" height="2" fill="#fff"/></svg></i></div>

<section class="data-panel">
  <svg class="refresh" width="22" height="22" viewBox="0 0 22 22"><path d="M4 9 A8 8 0 0 1 18 7 M18 13 A8 8 0 0 1 4 15" fill="none" stroke="#1b7fd1" stroke-width="2.5"/><path d="M18 2 V8 H12" fill="none" stroke="#1b7fd1" stroke-width="2.5"/><path d="M4 20 V14 H10" fill="none" stroke="#1b7fd1" stroke-width="2.5"/></svg>
  <table>
    <thead><tr><th>#</th><th>Gasday</th><th>Location</th><th>Loc_name</th><th>Flow_ind</th><th>Loc_Desc</th><th>Op_cap</th><th>Sch_cap</th><th>Op_avail_cap</th></tr></thead>
    <tbody>
      <tr><td>1</td><td>Lorem ipsum</td><td>Lorem ipsum</td><td>Lorem ipsum</td><td>Lorem ipsum</td><td>Lorem ipsum</td><td>Lorem ipsum</td><td>Lorem ipsum</td><td>Lorem ipsum</td></tr>
      <tr><td>2</td><td>Lorem ipsum</td><td>Lorem ipsum</td><td>Lorem ipsum</td><td>Lorem ipsum</td><td>Lorem ipsum</td><td>Lorem ipsum</td><td>Lorem ipsum</td><td>Lorem ipsum</td></tr>
      <tr><td>3</td><td>Lorem Ipsum</td><td>Lorem Ipsum</td><td>Lorem Ipsum</td><td>Lorem Ipsum</td><td>Lorem Ipsum</td><td>Lorem Ipsum</td><td>Lorem Ipsum</td><td>Lorem Ipsum</td></tr>
      <tr><td>4</td><td>Lorem Ipsum</td><td>Lorem Ipsum</td><td>Lorem Ipsum</td><td>Lorem Ipsum</td><td>Lorem Ipsum</td><td>Lorem Ipsum</td><td>Lorem Ipsum</td><td>Lorem Ipsum</td></tr>
      <tr><td>5</td><td>Lorem ipsum</td><td>Lorem ipsum</td><td>Lorem ipsum</td><td>Lorem ipsum</td><td>Lorem ipsum</td><td>Lorem ipsum</td><td>Lorem ipsum</td><td>Lorem ipsum</td></tr>
      <tr><td>6</td><td>Lorem ipsum</td><td>Lorem ipsum</td><td>Lorem ipsum</td><td>Lorem ipsum</td><td>Lorem ipsum</td><td>Lorem ipsum</td><td>Lorem ipsum</td><td>Lorem ipsum</td></tr>
      <tr><td>7</td><td>Lorem Ipsum</td><td>Lorem Ipsum</td><td>Lorem Ipsum</td><td>Lorem Ipsum</td><td>Lorem Ipsum</td><td>Lorem Ipsum</td><td>Lorem Ipsum</td><td>Lorem Ipsum</td></tr>
      <tr><td>8</td><td>Lorem Ipsum</td><td>Lorem Ipsum</td><td>Lorem Ipsum</td><td>Lorem Ipsum</td><td>Lorem Ipsum</td><td>Lorem Ipsum</td><td>Lorem Ipsum</td><td>Lorem Ipsum</td></tr>
      <tr><td>9</td><td>Lorem ipsum</td><td>Lorem ipsum</td><td>Lorem ipsum</td><td>Lorem ipsum</td><td>Lorem ipsum</td><td>Lorem ipsum</td><td>Lorem ipsum</td><td>Lorem ipsum</td></tr>
      <tr><td>10</td><td>Lorem ipsum</td><td>Lorem ipsum</td><td>Lorem ipsum</td><td>Lorem ipsum</td><td>Lorem ipsum</td><td>Lorem ipsum</td><td>Lorem ipsum</td><td>Lorem ipsum</td></tr>
      <tr><td>11</td><td>Lorem Ipsum</td><td>Lorem Ipsum</td><td>Lorem Ipsum</td><td>Lorem Ipsum</td><td>Lorem Ipsum</td><td>Lorem Ipsum</td><td>Lorem Ipsum</td><td>Lorem Ipsum</td></tr>
      <tr><td>12</td><td>Lorem Ipsum</td><td>Lorem Ipsum</td><td>Lorem Ipsum</td><td>Lorem Ipsum</td><td>Lorem Ipsum</td><td>Lorem Ipsum</td><td>Lorem Ipsum</td><td>Lorem Ipsum</td></tr>
    </tbody>
  </table>
</section>

<nav class="pager">
  <span class="pg on">1</span><span class="pg">2</span><span class="pg">3</span><span class="pg">4</span><span class="pg">5</span><span class="pg">6</span><span class="pg">7</span><span class="pg">8</span><span class="pg">9</span><span class="pg">10</span><span class="pg">11</span><span class="pg next">Next</span>
</nav>

<div class="chart-tabs">
  <div class="tab-head">Charts</div>
  <div class="tab">LOREM IPSUM</div>
  <div class="tab on">LOREM IPSUM</div>
  <div class="tab">LOREM IPSUM</div>
  <div class="tab">LOREM IPSUM</div>
</div>

<section class="chart-panel">
  <svg width="676" height="317" viewBox="0 0 770 360" font-family="Open Sans, sans-serif">
    <text x="18" y="41" font-size="30" fill="#333">LOCATION</text>
    <text x="18" y="65" font-size="11" fill="#888">FLOW</text>
    <text x="490" y="41" font-size="28" fill="#333" text-anchor="end">34.54</text>
    <text x="490" y="65" font-size="11" fill="#888" text-anchor="end">LAST CLOSE</text>
    <text x="610" y="41" font-size="28" fill="#ef3e4a" text-anchor="end">-0.08</text>
    <text x="610" y="65" font-size="11" fill="#888" text-anchor="end">CHANGE</text>
    <text x="750" y="41" font-size="28" fill="#ef3e4a" text-anchor="end">-1.25%</text>
    <text x="750" y="65" font-size="11" fill="#888" text-anchor="end">% CHANGE</text>
    <g stroke="#dcdcdc" stroke-width="1">
      <line x1="44" y1="104" x2="750" y2="104"/>
      <line x1="44" y1="154" x2="750" y2="154"/>
      <line x1="44" y1="204" x2="750" y2="204"/>
      <line x1="44" y1="254" x2="750" y2="254"/>
      <line x1="44" y1="304" x2="750" y2="304"/>
      <line x1="44" y1="96" x2="44" y2="304"/>
    </g>
    <g font-size="11" fill="#777">
      <text x="20" y="104">36</text><text x="20" y="154">32</text><text x="20" y="204">28</text><text x="20" y="254">28</text>
    </g>
    <path fill="#c59fdc" d="M44 128 C70 115 95 110 110 113 C135 116 145 128 170 133 C200 140 230 145 250 153 C280 163 295 180 310 185 C330 180 340 178 360 177 C390 174 410 170 430 160 C445 150 452 138 460 138 C470 140 490 165 500 178 C520 198 535 215 550 223 C565 232 580 231 595 228 C625 222 638 220 645 190 C650 150 660 135 678 128 C695 124 700 143 708 140 C715 135 722 132 729 131 L729 304 L44 304 Z"/>
    <g font-size="11" fill="#777" text-anchor="middle">
      <text x="70" y="330">JUN</text><text x="122" y="330">JUL</text><text x="176" y="330">AUG</text><text x="231" y="330">SEP</text><text x="285" y="330">OCT</text><text x="341" y="330">NOV</text><text x="398" y="330">DEC</text><text x="451" y="330">JAN</text><text x="503" y="330">FEB</text><text x="559" y="330">MAR</text><text x="614" y="330">APR</text><text x="669" y="330">MAY</text><text x="723" y="330">JUN</text>
    </g>
  </svg>
</section>

<footer class="footer">
  <div><b>Copyright 2014</b> - Northwind Gas Co. All Right Reserved // Cedar Falls, UT 84120 // (555) 014-2290</div>
  <nav>ABOUT &nbsp;|&nbsp; BLOG &nbsp;|&nbsp; CONTACT</nav>
</footer>

</body>
</html>
```